Packaging for new retail dips "Quellmor"

* We require packaging for our new retail dip range.
* We have a small "Our Story" write up that we would like somewhere...
* We have approx. 7 different flavours - Hommous, Mediterranean Olive, Beetroot, Tzatziki etc. We would like one design where we can change the colour panel and the name of the dip.
* We are looking for a modern, clean, gourmet looking design - not the usual dip packaging you see on supermarket shelves.
* See my inspiration photo's.
* The Dieline attached is to scale.
Updates
Project Deadline Extended
Reason: Extension due to Dielines and Measurements not uploaded when we thought they were.
Target Market(s)
Will be going into retail supermarkets.
Industry/Entity Type
Retail
Font styles to use
Colors
Designer to choose colors to be used in the design.
Requirements
Must have
- * Please use our 'Quellmor' logo on the front and on the front side (if possible).
Nice to have
- * 'taste is everything' somewhere...
Should not have
- * No photo's of dips or photo's in general.

```html
<!DOCTYPE html>
<html lang="en">
<head>
<meta charset="utf-8">
<title>Quellmor Dip Range Packaging</title>
<link rel="stylesheet" href="https://fonts.googleapis.com/css2?family=Caveat+Brush&family=Raleway:wght@300&family=PT+Serif:wght@700&display=swap">
<style>
  :root {
    --canvas: #ffffff;
    --label-white: #f1f2f3;
    --gold-dark: #b8892a;
    --gold-light: #f3e4a6;
    --olive-light: #8cc760;
    --olive-mid: #6fb84a;
    --olive-dark: #4ea33b;
    --olive-box: #3a6b2a;
    --olive-ink: #2f4a1f;
    --sky-light: #4aa8e0;
    --sky-mid: #2a94d6;
    --sky-dark: #1f88cf;
    --sky-box: #1740a0;
    --sky-ink: #3b4a1e;
    --logo-ink: #4a4a4a;
  }
  * { box-sizing: border-box; margin: 0; padding: 0; }
  html, body { width: 1200px; height: 960px; overflow: hidden; background: var(--canvas); }
  .range { position: relative; width: 1200px; height: 960px; }
  .sleeve {
    position: absolute;
    top: 286px;
    width: 404px;
    height: 440px;
    overflow: hidden;
    box-shadow: 0 2px 6px rgba(0,0,0,0.12);
  }
  .sleeve--olive { left: 152px; }
  .sleeve--tzatziki { left: 666px; }
  .sleeve__art { position: absolute; inset: 0; width: 404px; height: 440px; }

  .brand {
    position: absolute;
    left: 104px;
    top: 74px;
    width: 180px;
    text-align: center;
    font-family: "Raleway", sans-serif;
    font-weight: 300;
    font-size: 26px;
    letter-spacing: 1px;
    color: var(--logo-ink);
    line-height: 1;
  }

  .flavour {
    position: absolute;
    left: 88px;
    top: 194px;
    width: 222px;
    height: 96px;
    text-align: center;
    color: #ffffff;
    font-family: "Caveat Brush", cursive;
    padding-top: 12px;
    line-height: 1;
  }
  .sleeve--olive .flavour { background: var(--olive-box); }
  .sleeve--tzatziki .flavour { background: var(--sky-box); }
  .flavour::after {
    content: "";
    position: absolute;
    left: 0; right: 0; bottom: -4px;
    height: 4px;
    background: #ffffff;
    border-radius: 0 0 50% 50% / 0 0 100% 100%;
  }
  .flavour__range { font-size: 25px; display: block; }
  .flavour__name { font-size: 38px; display: block; margin-top: 4px; }

  .weight {
    position: absolute;
    left: 306px;
    top: 406px;
    font-family: "PT Serif", serif;
    font-weight: 700;
    font-size: 17px;
  }
  .sleeve--olive .weight { color: var(--olive-ink); }
  .sleeve--tzatziki .weight { color: var(--sky-ink); left: 300px; top: 404px; }
</style>
</head>
<body>
<main class="range">

  <section class="sleeve sleeve--olive">
    <svg class="sleeve__art" viewBox="0 0 404 440" xmlns="http://www.w3.org/2000/svg">
      <defs>
        <linearGradient id="olive-field" x1="0" y1="0" x2="1" y2="0">
          <stop offset="0" stop-color="var(--olive-light)"/>
          <stop offset="0.5" stop-color="var(--olive-mid)"/>
          <stop offset="1" stop-color="var(--olive-dark)"/>
        </linearGradient>
        <linearGradient id="gold-band-a" x1="0" y1="0" x2="1" y2="0">
          <stop offset="0" stop-color="var(--gold-dark)"/>
          <stop offset="0.45" stop-color="var(--gold-light)"/>
          <stop offset="0.75" stop-color="var(--gold-dark)"/>
          <stop offset="1" stop-color="var(--gold-light)"/>
        </linearGradient>
      </defs>
      <rect class="label-top" width="404" height="440" fill="var(--label-white)"/>
      <path class="colour-panel" role="img" aria-label="Soft leaf pattern on the flavour colour panel"
            d="M0 170 C 110 176, 220 130, 404 96 L404 440 L0 440 Z" fill="url(#olive-field)"/>
      <path class="gold-band" d="M0 132 C 110 146, 220 106, 404 62 L404 80 C 220 122, 110 170, 0 164 Z" fill="url(#gold-band-a)"/>
      <path class="white-edge" d="M0 164 C 110 170, 220 122, 404 80 L404 96 C 220 130, 110 176, 0 170 Z" fill="#ffffff"/>
      <circle class="seal" cx="61" cy="82" r="35" fill="var(--gold-dark)"/>
      <circle class="seal__inner" cx="61" cy="82" r="26" fill="#ffffff"/>
    </svg>
    <div class="brand">QUELLMOR</div>
    <div class="flavour">
      <span class="flavour__range">Mediterranean</span>
      <span class="flavour__name">Olive</span>
    </div>
    <div class="weight">200 g</div>
  </section>

  <section class="sleeve sleeve--tzatziki">
    <svg class="sleeve__art" viewBox="0 0 404 440" xmlns="http://www.w3.org/2000/svg">
      <defs>
        <linearGradient id="sky-field" x1="0" y1="0" x2="1" y2="0">
          <stop offset="0" stop-color="var(--sky-light)"/>
          <stop offset="0.5" stop-color="var(--sky-mid)"/>
          <stop offset="1" stop-color="var(--sky-dark)"/>
        </linearGradient>
        <linearGradient id="gold-band-b" x1="0" y1="0" x2="1" y2="0">
          <stop offset="0" stop-color="var(--gold-dark)"/>
          <stop offset="0.45" stop-color="var(--gold-light)"/>
          <stop offset="0.75" stop-color="var(--gold-dark)"/>
          <stop offset="1" stop-color="var(--gold-light)"/>
        </linearGradient>
      </defs>
      <rect class="label-top" width="404" height="440" fill="var(--label-white)"/>
      <path class="colour-panel" role="img" aria-label="Soft leaf pattern on the flavour colour panel"
            d="M0 170 C 110 176, 220 130, 404 96 L404 440 L0 440 Z" fill="url(#sky-field)"/>
      <path class="gold-band" d="M0 132 C 110 146, 220 106, 404 62 L404 80 C 220 122, 110 170, 0 164 Z" fill="url(#gold-band-b)"/>
      <path class="white-edge" d="M0 164 C 110 170, 220 122, 404 80 L404 96 C 220 130, 110 176, 0 170 Z" fill="#ffffff"/>
      <circle class="seal" cx="61" cy="82" r="35" fill="var(--gold-dark)"/>
      <circle class="seal__inner" cx="61" cy="82" r="26" fill="#ffffff"/>
    </svg>
    <div class="brand">QUELLMOR</div>
    <div class="flavour">
      <span class="flavour__range">Mediterranean</span>
      <span class="flavour__name">Tzatziki</span>
    </div>
    <div class="weight">200 g</div>
  </section>

</main>
</body>
</html>
```